KVT Wellness Co Business Card for food and Beverage Falcons & Lanterns

One main business card design for a wellness enterprise which represents two brands. We need one primary card design, for two different employees. The only difference between the cards will be the name, title and phone number for each employee, all other design elements will be same.
I've uploaded the logos for each brand. I have also uploaded a mockup which I made using Google's drawing tool. I can provide example images of business cards we find attractive if you would like some help picturing what we like.
I'm picturing the color splash on the back of the card below the two logos to be a dark burgundy or blue. This may sound a bit silly but the feel of the card and color should look almost like wizard dress robes. Dark emerald green, dark blue and dark burgundy with black undertones and gold lace.
Updates

Reason: Thank you all for the submissions. I will need some extra time to give you feedback. Cheers

Target Market(s)

Healthy food and beverage industry

Industry/Entity Type

Health And Wellness

Contact Information for Business Card

On one side we would like the business name, location, title of employee, employee name and contact details. On the flip side we would like our two brand logos and a splash of color. We would like the card to have a black font with some gold accents if possible. We would also like the trim of the business card or a middle ply within the card stock to have a color other than white.

Font styles to use
Serif

Colors
ec1f27
0255a3
00a990

Requirements
Must have
• Bold dark colors, happy to provide sample photos of business cards I like from clipnook. Must have a version for two different employees. Must be sharp, modern and chic.
Nice to have
• Thick card stock layer in between the front and back of card that is either black or gold lace or something to make it feel, well let's say to make it feel expensive.
Should not have
• Should not have any cartoon-ey elements. All business.

```html
<!DOCTYPE html>
<html lang="en">
<head>
<meta charset="utf-8">
<title>KVT Wellness Co — Business Card</title>
<link href="https://fonts.googleapis.com/css2?family=Share+Tech&family=Noto+Serif:wght@400&display=swap" rel="stylesheet">
<style>
  :root {
    --backdrop: #31343a;
    --card-black: #2a2c30;
    --panel-black: #26282c;
    --gold: #b47c46;
    --bronze: #6a5135;
    --bronze-deep: #4a3722;
    --bronze-light: #7d613f;
    --divider: #6a6c70;
    --mark-ink: #121214;
  }
  * { margin: 0; padding: 0; box-sizing: border-box; }
  html, body { width: 1200px; height: 1200px; overflow: hidden; }
  body { background: var(--backdrop); position: relative; font-family: "Noto Serif", Georgia, serif; }

  .card { position: absolute; width: 840px; height: 480px; overflow: hidden; }
  .card-front { left: 54px; top: 88px; background: var(--card-black); }
  .card-back { left: 298px; top: 620px; background: var(--bronze); }

  .company { position: absolute; left: 0; width: 428px; text-align: center; white-space: nowrap;
    font-family: "Share Tech", "Arial Narrow", sans-serif; color: var(--gold); }
  .company-name { top: 208px; font-size: 33px; letter-spacing: 3px; }
  .company-location { top: 266px; font-size: 22px; letter-spacing: 2px; }

  .divider { position: absolute; left: 422px; top: 124px; width: 1px; height: 252px; background: var(--divider); }

  .contact { position: absolute; left: 436px; width: 340px; text-align: center; white-space: nowrap; color: var(--gold); }
  .contact-name { top: 176px; font-size: 20px; letter-spacing: 1px; }
  .contact-title { top: 214px; font-size: 10px; letter-spacing: 0.5px; }
  .contact-phone { top: 260px; font-size: 13px; letter-spacing: 0.5px; }
  .contact-email { top: 300px; font-size: 14px; }

  .brand-panel { position: absolute; left: 0; top: 0; width: 238px; height: 480px; background: var(--panel-black); }
  .brand-mark { position: absolute; left: 16px; width: 206px; text-align: center;
    font-family: "Noto Serif", Georgia, serif; color: var(--mark-ink); letter-spacing: 1px; line-height: 1.3; }
  .brand-mark-primary { top: 78px; font-size: 30px; }
  .brand-mark-secondary { top: 328px; font-size: 19px; }

  .back-company { position: absolute; left: 238px; width: 484px; text-align: center; white-space: nowrap;
    font-family: "Share Tech", "Arial Narrow", sans-serif; color: var(--bronze-deep);
    text-shadow: 1px 1px 0 var(--bronze-light), -1px -1px 0 rgba(0,0,0,0.25); }
  .back-company-name { top: 198px; font-size: 33px; letter-spacing: 3px; }
  .back-company-location { top: 264px; font-size: 22px; letter-spacing: 2px; }

  .splash { position: absolute; left: 646px; top: 302px; width: 160px; height: 130px;
    border-radius: 50%; background: radial-gradient(circle at 55% 50%, var(--bronze-light) 0 22%, rgba(74,55,34,0.55) 30%, rgba(106,81,53,0) 68%); }
</style>
</head>
<body>
  <section class="card card-front">
    <div class="company company-name">KVT Wellness Co</div>
    <div class="company company-location">Larkvale, CA</div>
    <div class="divider"></div>
    <div class="contact contact-name">Marcus Hale</div>
    <div class="contact contact-title">Beverage Alchemist</div>
    <div class="contact contact-phone">415.555.0182</div>
    <div class="contact contact-email">kvtwellnessco@mailbox.com</div>
  </section>

  <section class="card card-back">
    <div class="brand-panel">
      <div class="brand-mark brand-mark-primary">KVT</div>
      <div class="brand-mark brand-mark-secondary">Falcons &amp; Lanterns</div>
    </div>
    <div class="back-company back-company-name">KVT Wellness Co</div>
    <div class="back-company back-company-location">Larkvale, CA</div>
    <div class="splash" role="img" aria-label="Embossed ink splash decoration"></div>
  </section>
</body>
</html>
```